K7 Electrical Services Ltd Web design

I require a web site for my new electrical contracting company. We are customer service orientated. Offering high value electrical installations, design and maintenance. Focused on custom residential and commercial upgrading. Lighting design and application are paramount in our company's services. Industry leading product use and integration are always on the forefront with our customer client services. As well as energy efficiency.

Target Market(s)

Homebuilders, General Contractors, Property management companies, clients, individuals,

Industry/Entity Type

Electric Company

Coding

Coded - Design and coding required

Number of Pages Required

3 page

Requirements
Must have
• Classic, modern, edgy but not trendy . Appeals to the masse.
• 3 page
• home page
• about page
• gallery page
• ability to contact from the webiste
Nice to have
• open to all types of designs that are relative to the construction industry.
• Black, Grey, metallic ice blue and deep purple colours from the logo.
Should not have
• anything cheesy with cartoon light bulb images.

```html
<!DOCTYPE html>
<html lang="en">
<head>
<meta charset="utf-8">
<title>K7 Electrical Services Ltd</title>
<link href="https://fonts.googleapis.com/css2?family=Orbitron:wght@700&family=Open+Sans:ital,wght@0,300;0,400;0,600;1,400&display=swap" rel="stylesheet">
<style>
:root{
  --purple:#6a2f94;
  --purple-bright:#9b2fd6;
  --ink:#333333;
  --muted:#7a7a7a;
  --line:#dddddd;
  --topbar:#f7f7f7;
  --footer:#242424;
  --field:#9a9a9a;
  --social:#3d3d3d;
  --white:#ffffff;
}
*{box-sizing:border-box;margin:0;padding:0}
html,body{width:1200px;height:2390px;overflow:hidden}
body{position:relative;background:var(--white);font-family:"Open Sans",Arial,sans-serif;color:var(--ink)}
.abs{position:absolute}

/* top bar */
.topbar{left:0;top:0;width:1200px;height:48px;background:var(--topbar)}
.topbar-text{left:160px;top:16px;font-size:11px;color:var(--muted);text-transform:uppercase}
.search-btn{left:991px;top:0;width:49px;height:48px;background:var(--purple);display:flex;align-items:center;justify-content:center}

/* header */
.header{left:0;top:48px;width:1200px;height:108px;background:var(--white)}
.brand{left:160px;top:88px;font-size:20px;font-weight:600;color:var(--purple);white-space:nowrap;display:flex;align-items:center;gap:10px}
.brand-dot{width:14px;height:14px;background:var(--purple);flex:none}
.header-phone{left:765px;top:86px;font-size:22px;font-weight:300;color:#666;display:flex;align-items:center;gap:8px}
.lang{left:982px;top:74px;width:58px;height:58px;border:1.5px solid #333;border-radius:50%;font-size:12px;font-weight:600;color:#333;display:flex;align-items:center;justify-content:center;gap:3px}

/* navigation */
.nav{left:0;top:156px;width:1200px;height:64px;background:var(--purple);border-top:2px solid #d8cfe0}
.nav a{position:absolute;top:24px;color:var(--white);font-size:12px;text-decoration:none;text-transform:uppercase}

/* hero */
.hero{left:0;top:220px;width:1200px;height:545px;background:linear-gradient(90deg,#e4e6e8 0%,#d6dadd 45%,#cfd3d6 100%)}
.hero-caption{left:0;top:670px;width:1200px;height:95px;background:rgba(95,95,95,.85);display:flex;align-items:center;justify-content:center}
.hero-caption h1{font-family:"Orbitron",sans-serif;font-weight:700;font-size:36px;color:var(--white);letter-spacing:1px}

/* welcome */
.welcome-title{left:0;top:828px;width:1200px;text-align:center;font-size:32px;font-weight:300;color:#333}
.welcome-sub{left:0;top:876px;width:1200px;text-align:center;font-size:17px;color:#333}
.divider{left:0;top:932px;width:1200px;height:1px;background:var(--line)}
.divider-icon{left:584px;top:914px;width:32px;height:40px;background:var(--white)}
.intro{left:190px;top:973px;width:820px;text-align:center;font-size:13px;font-style:italic;line-height:21px;color:var(--muted)}
.mini-brand{left:0;top:1070px;width:1200px;text-align:center;font-size:13px;font-weight:600;color:var(--purple)}
.offer-title{left:0;top:1122px;width:1200px;text-align:center;font-size:18px;font-weight:400;color:#333}
.offer-box{left:160px;top:1173px;width:880px;height:110px;background:var(--purple);border:1.5px solid #4a1f6a;color:var(--white);font-size:12px;line-height:18px;text-align:center;padding:28px 40px 0}

/* gallery */
.gallery{left:0;top:1357px;width:1200px;height:540px;background:linear-gradient(135deg,#4a4a4a 0%,#3a3a3a 50%,#555 100%)}
.gallery-title{left:158px;top:1410px;font-size:31px;font-weight:300;color:var(--white)}
.card{top:1476px;height:282px}
.card-photo{width:100%;height:218px}
.card-label{height:64px;font-size:24px;font-weight:300;display:flex;align-items:center;padding-left:16px;white-space:nowrap}
.card-label.active{background:rgba(120,120,120,.85);color:var(--white)}
.card-label.plain{background:var(--white);color:#555}
.arrow{width:26px;height:26px;border-radius:50%;display:flex;align-items:center;justify-content:center}
.arrow-prev{left:107px;top:1591px;background:var(--purple-bright)}
.arrow-next{left:1065px;top:1591px;background:var(--white)}

/* footer */
.footer{left:0;top:1897px;width:1200px;height:493px;background:var(--footer)}
.footer-bar{left:160px;top:1897px;width:880px;height:8px;background:var(--purple)}
.footer-heading{top:1945px;font-size:13px;font-weight:600;color:var(--white);text-transform:uppercase}
.address{left:160px;top:1976px;width:230px;font-size:11.5px;line-height:21px;color:#bdbdbd}
.address p+p{margin-top:21px}
.address b{color:var(--white);font-weight:600;display:inline-block;width:42px}
.quick-links{left:450px;top:1974px;list-style:none;font-size:11.5px;line-height:22.5px;color:#bdbdbd}
.quick-links li::before{content:"";display:inline-block;width:5px;height:5px;background:var(--purple-bright);margin-right:9px;vertical-align:middle}
.field{background:var(--field);font-size:11px;color:#222;padding-left:12px;display:flex;align-items:center}
.field-area{align-items:flex-start;padding-top:12px}
.send{left:669px;top:2168px;width:112px;height:46px;border:1.5px solid var(--purple);color:var(--purple-bright);font-size:11px;display:flex;align-items:center;justify-content:center}
.copyright{left:660px;top:2242px;width:380px;text-align:right;font-size:11px;color:#9a9a9a}
.footer-brand{left:160px;top:2243px;width:240px;height:92px;background:var(--white);display:flex;align-items:center;justify-content:center;text-align:center;font-size:17px;font-weight:600;color:var(--purple);line-height:1.2;padding:0 12px}
.social{top:2276px;width:62px;height:62px;border-radius:50%;background:var(--social);display:flex;align-items:center;justify-content:center}
.social span{width:12px;height:12px;border-radius:50%;background:var(--white)}
</style>
</head>
<body>

<div class="abs topbar"></div>
<div class="abs topbar-text">Welcome to the electrical services</div>
<div class="abs search-btn">
  <svg width="16" height="16" viewBox="0 0 16 16"><circle cx="6.5" cy="6.5" r="4.5" fill="none" stroke="#fff" stroke-width="2"/><line x1="10" y1="10" x2="14" y2="14" stroke="#fff" stroke-width="2.4" stroke-linecap="round"/></svg>
</div>

<header class="abs header"></header>
<div class="abs brand"><span class="brand-dot"></span><span>K7 Electrical Services Ltd</span></div>
<div class="abs header-phone">
  <svg width="14" height="24" viewBox="0 0 14 24"><path d="M4 2 L8 2 L8 7 L5.5 8 Q5 12 5.5 16 L8 17 L8 22 L4 22 Q1 12 4 2 Z" fill="#888"/></svg>
  001-555-0147
</div>
<div class="abs lang">EN
  <svg width="8" height="6" viewBox="0 0 8 6"><path d="M1 1 L4 4 L7 1" fill="none" stroke="#333" stroke-width="1.5"/></svg>
</div>

<nav class="abs nav">
  <a href="#" style="left:174px">Home</a>
  <a href="#" style="left:271px">About Us</a>
  <a href="#" style="left:392px">Gallery</a>
  <a href="#" style="left:504px">Contact Us</a>
</nav>

<div class="abs hero" role="img" aria-label="Smiling electrician in blue overalls giving a thumbs up in a bright living room"></div>
<div class="abs hero-caption"><h1>LOREM IPSUM DOLOR SIT AMET.</h1></div>

<h2 class="abs welcome-title">Welcome To The Electrical Services</h2>
<p class="abs welcome-sub">Ut enim ad minim veniam, quis nostrud exercitation ullamco laboris nisi ut aliquip ex</p>
<div class="abs divider"></div>
<div class="abs divider-icon">
  <svg width="32" height="40" viewBox="0 0 32 40"><line x1="9" y1="34" x2="23" y2="6" stroke="var(--purple)" stroke-width="2"/><line x1="13" y1="35" x2="26" y2="9" stroke="var(--purple)" stroke-width="1.2"/></svg>
</div>
<p class="abs intro">Lorem ipsum dolor sit amet, consectetur adipiscing elit, sed do eiusmod tempor incididunt ut labore et dolore magna aliqua. Ut enim ad minim veniam, quis nostrud exercitation ullamco laboris nisi ut aliquip ex ea commodo consequat. Duis aute irure dolor in reprehenderit in voluptate velit esse cillum dolore eu fugiat nulla pariatur.</p>
<div class="abs mini-brand">K7 Electrical Services Ltd</div>
<h3 class="abs offer-title">We Offer...</h3>
<div class="abs offer-box">Lorem ipsum dolor sit amet, consectetur adipiscing elit, sed do eiusmod tempor incididunt ut labore et dolore magna aliqua. Ut enim ad minim veniam, quis nostrud exercitation ullamco laboris nisi ut aliquip ex ea commodo consequat. Duis aute irure dolor in reprehenderit in voluptate velit esse cillum dolore eu fugiat nulla pariatur.</div>

<section class="abs gallery" role="img" aria-label="Dimmed background photo of electricians at work on a ladder"></section>
<h2 class="abs gallery-title">Electrical Services Gallery</h2>

<div class="abs card" style="left:160px;width:285px">
  <div class="card-photo" role="img" aria-label="Electrician in hard hat wiring a network cabinet" style="background:linear-gradient(135deg,#7f8c92,#b9c2c6)"></div>
  <div class="card-label active">Lorem Ipsum Dolor</div>
</div>
<div class="abs card" style="left:456px;width:287px">
  <div class="card-photo" role="img" aria-label="Electrician kneeling with plans beside a switchboard" style="background:linear-gradient(135deg,#5e6a78,#c8b46a)"></div>
  <div class="card-label plain">Ipsum Dolor Sit Amet</div>
</div>
<div class="abs card" style="left:752px;width:288px">
  <div class="card-photo" role="img" aria-label="Hands holding pliers cutting a cable" style="background:linear-gradient(135deg,#e6e6e6,#9aa6b8)"></div>
  <div class="card-label plain">Dolor Sit Amet Consect</div>
</div>
<div class="abs arrow arrow-prev"><svg width="8" height="8" viewBox="0 0 8 8"><path d="M6 1 L2 4 L6 7 Z" fill="#fff"/></svg></div>
<div class="abs arrow arrow-next"><svg width="8" height="8" viewBox="0 0 8 8"><path d="M2 1 L6 4 L2 7 Z" fill="#333"/></svg></div>

<footer class="abs footer" role="img" aria-label="Dark background photo of an electrician at work"></footer>
<div class="abs footer-bar"></div>
<h3 class="abs footer-heading" style="left:160px">Contact Address</h3>
<h3 class="abs footer-heading" style="left:450px">Quick Links</h3>
<h3 class="abs footer-heading" style="left:669px">Contact Us</h3>
<div class="abs address">
  <p>Lorem ipsum dolor sit amet, consectetur adipiscing elit, sed do eiusmod tempor incididunt ut labore et dolore magna aliqua. Ut enim ad minim veniam.</p>
  <p>Lorem Ipsum Dolor Sit Amet Consectetor<br>Dolor Sit Amet Consectetor<br>
  <b>Telp</b>: 001 555 0148 / 012 555 0149<br>
  <b>Fax</b>: 012 555 0150<br>
  <b>Email</b>: info@k7electrical.example</p>
</div>
<ul class="abs quick-links">
  <li>Home</li><li>About Us</li><li>Services</li><li>Gallery</li><li>Contact Us</li>
</ul>
<div class="abs field" style="left:669px;top:1996px;width:177px;height:40px">Name</div>
<div class="abs field" style="left:862px;top:1996px;width:178px;height:40px">Email</div>
<div class="abs field field-area" style="left:669px;top:2052px;width:371px;height:96px">How Can We Help?</div>
<div class="abs send">SEND</div>
<div class="abs copyright">© 2018 Electrical Services Allrights are Reserved.</div>
<div class="abs footer-brand">K7 Electrical Services Ltd</div>
<div class="abs social" style="left:755px"><span></span></div>
<div class="abs social" style="left:828px"><span></span></div>
<div class="abs social" style="left:902px"><span></span></div>
<div class="abs social" style="left:975px"><span></span></div>

</body>
</html>
```